Business card revamp

we are refrigeration mechanic i need a modern professional double side business card using my current branding
The card information must have site address~ 17 Whitlow st marlowe, Vic 3712 postal address~ P.o. Box 862 marlowe,Vic 3711 Phone Number~0358149637 Fax Nunber~0358260518 Email address~ brucet@pelvanor.com.au Title~ Manager Licence numbers~ AU47391, NSW 681329K Web site~ www.frostrimvane.com.au

Industry/Entity Type

Business

```html
<!DOCTYPE html>
<html lang="en">
<head>
<meta charset="utf-8">
<title>Frostrim Vane – Business Card</title>
<link rel="stylesheet" href="https://fonts.googleapis.com/css2?family=Arimo:wght@400;700&display=swap">
<style>
  :root {
    --stage: #2b2b2b;
    --paper: #ffffff;
    --paper-shade: #f1f1f1;
    --back-card: #3a3a3a;
    --back-card-edge: #2f2f2f;
    --ink: #2a2a2a;
    --ink-soft: #6e6e6e;
    --brand-blue: #2b86d0;
    --brand-red: #d8262f;
    --back-text: #e2e2e2;
    --back-text-soft: #a9a9a9;
  }
  * { box-sizing: border-box; margin: 0; padding: 0; }
  html, body {
    width: 1200px; height: 1000px; overflow: hidden;
    background: var(--stage);
    font-family: "Arimo", Arial, sans-serif;
  }
  .sheet {
    width: 1200px; height: 1000px;
    display: flex; flex-direction: column; align-items: center; justify-content: center;
    gap: 60px;
  }
  .card {
    position: relative;
    width: 700px; height: 400px;
    border-radius: 4px;
    overflow: hidden;
  }
  /* Front */
  .card--front {
    background: linear-gradient(180deg, var(--paper) 0%, var(--paper-shade) 100%);
    color: var(--ink);
  }
  .brand {
    position: absolute; left: 46px; top: 82px;
  }
  .brand__row { display: flex; align-items: center; gap: 10px; }
  .brand__dot {
    width: 16px; height: 16px; border-radius: 50%;
    background: var(--brand-blue);
  }
  .brand__name {
    font-weight: 700; font-size: 32px; letter-spacing: 1px;
    color: var(--brand-red); text-transform: uppercase;
  }
  .brand__tagline {
    margin-top: 6px; margin-left: 26px;
    font-size: 10px; letter-spacing: 1.6px; color: var(--ink-soft);
    text-transform: uppercase;
  }
  .holder {
    position: absolute; right: 52px; top: 58px; text-align: right;
  }
  .holder__name { font-size: 22px; font-weight: 700; letter-spacing: 1px; }
  .holder__first { color: var(--brand-blue); }
  .holder__last { color: var(--ink-soft); }
  .holder__role { margin-top: 4px; font-size: 16px; letter-spacing: 3px; color: var(--ink-soft); }
  .tab {
    position: absolute; right: 0; top: 58px;
    width: 22px; height: 40px; background: var(--brand-red);
  }
  .postal {
    position: absolute; right: 52px; top: 160px; text-align: right;
    font-size: 16px; letter-spacing: 1px; line-height: 1.45;
  }
  .postal__label { color: var(--brand-blue); font-weight: 700; }
  .postal__value { color: var(--ink); margin-bottom: 8px; }
  .postal__value--soft { color: var(--ink-soft); }
  .contacts {
    position: absolute; left: 46px; bottom: 40px;
    list-style: none; font-size: 19px; letter-spacing: 1.5px; color: var(--ink);
  }
  .contacts__item { display: flex; align-items: flex-start; gap: 12px; margin-top: 8px; }
  .contacts__icon { width: 16px; height: 16px; margin-top: 4px; flex: none; fill: var(--brand-blue); }
  .contacts__item--address { margin-top: 14px; line-height: 1.2; }
  /* Back */
  .card--back {
    background: linear-gradient(160deg, var(--back-card) 0%, var(--back-card-edge) 100%);
    color: var(--back-text);
    display: flex; flex-direction: column; align-items: center; justify-content: center;
  }
  .back-brand__name {
    font-weight: 700; font-size: 64px; letter-spacing: 3px;
    color: var(--back-text); text-transform: uppercase;
  }
  .back-brand__tagline {
    margin-top: 8px; font-size: 15px; letter-spacing: 3px;
    color: var(--back-text-soft); text-transform: uppercase;
  }
  .back-web {
    margin-top: 44px; font-size: 18px; letter-spacing: 4px; color: var(--back-text);
  }
</style>
</head>
<body>
<main class="sheet">
  <section class="card card--front" aria-label="Card front">
    <div class="brand">
      <div class="brand__row">
        <span class="brand__dot"></span>
        <span class="brand__name">Frostrim Vane</span>
      </div>
      <p class="brand__tagline">Heating and cooling specialists</p>
    </div>

    <div class="tab"></div>
    <div class="holder">
      <p class="holder__name"><span class="holder__first">Bruce</span><span class="holder__last">Tennaris</span></p>
      <p class="holder__role">Manager</p>
    </div>

    <div class="postal">
      <p class="postal__label">P.o. Box</p>
      <p class="postal__value">862 marlowe,Vic 3711</p>
      <p class="postal__label">Licence numbers</p>
      <p class="postal__value postal__value--soft">AU47391, NSW 681329K</p>
    </div>

    <ul class="contacts">
      <li class="contacts__item">
        <svg class="contacts__icon" viewBox="0 0 16 16" aria-hidden="true"><rect x="4" y="1" width="8" height="14" rx="1.5"/><rect x="5.5" y="3" width="5" height="8" fill="#fff"/></svg>
        <span>0358149637</span>
      </li>
      <li class="contacts__item">
        <svg class="contacts__icon" viewBox="0 0 16 16" aria-hidden="true"><rect x="4" y="1" width="8" height="4"/><rect x="1" y="6" width="14" height="6" rx="1"/><rect x="4" y="10" width="8" height="5" fill="#fff"/><rect x="4" y="10" width="8" height="1.5"/></svg>
        <span>0358260518</span>
      </li>
      <li class="contacts__item">
        <svg class="contacts__icon" viewBox="0 0 16 16" aria-hidden="true"><rect x="1" y="3" width="14" height="10"/><path d="M1.5 3.5 L8 9 L14.5 3.5" fill="none" stroke="#fff" stroke-width="1.4"/></svg>
        <span>brucet@pelvanor.com.au</span>
      </li>
      <li class="contacts__item contacts__item--address">
        <svg class="contacts__icon" viewBox="0 0 16 16" aria-hidden="true"><path d="M8 1 C4.7 1 3 3.4 3 5.8 C3 9.2 8 15 8 15 C8 15 13 9.2 13 5.8 C13 3.4 11.3 1 8 1 Z"/><circle cx="8" cy="6" r="2" fill="#fff"/></svg>
        <span>17 Whitlow st marlowe<br>Vic 3712</span>
      </li>
    </ul>
  </section>

  <section class="card card--back" aria-label="Card back">
    <p class="back-brand__name">Frostrim Vane</p>
    <p class="back-brand__tagline">Heating and cooling specialists</p>
    <p class="back-web">www.frostrimvane.com.au</p>
  </section>
</main>
</body>
</html>
```